Bright-loop designs Business Card

embroidery printing

Target Market(s)

Businesses and public

Industry/Entity Type

Business

Contact Information for Business Card

Front of card..... Bright-loop designs .... Corin Maltby..... 868 512-7361.... Email... bright_loopdesigns@mailbrook.net

Back of card..... Bright-loop designs embroidery & artwork

Colors
000000

```html
<!DOCTYPE html>
<html lang="en">
<head>
<meta charset="utf-8">
<title>Bright-loop designs — Business Card</title>
<link href="https://fonts.googleapis.com/css2?family=Arvo:wght@400;700&family=Arimo:wght@400;700&display=swap" rel="stylesheet">
<style>
  :root {
    --backdrop: #e9e4dc;
    --card-white: #ffffff;
    --brand-red: #8c1820;
    --ink: #000000;
    --muted: #6b6b6b;
    --on-red: #ffffff;
  }
  * { margin: 0; padding: 0; box-sizing: border-box; }
  html, body {
    width: 1200px;
    height: 1200px;
    overflow: hidden;
    background: var(--backdrop);
  }
  .canvas {
    position: relative;
    width: 1200px;
    height: 1200px;
  }
  .card {
    position: absolute;
    left: 187px;
    width: 887px;
    height: 514px;
    border-radius: 24px;
    box-shadow: 0 6px 18px rgba(0,0,0,0.18);
    overflow: hidden;
  }
  .card--front {
    top: 72px;
    background: var(--card-white);
    text-align: center;
  }
  .card--back {
    top: 614px;
    background: var(--brand-red);
    display: flex;
    flex-direction: column;
    align-items: center;
    justify-content: center;
    gap: 14px;
  }
  .wordmark {
    font-family: "Arvo", serif;
    font-weight: 700;
    white-space: nowrap;
    line-height: 1;
  }
  .wordmark--front {
    position: absolute;
    top: 106px;
    left: 0;
    right: 0;
    font-size: 44px;
    color: var(--ink);
  }
  .wordmark--back {
    font-size: 70px;
    color: var(--on-red);
  }
  .tagline {
    font-family: "Arvo", serif;
    font-weight: 700;
    font-size: 30px;
    letter-spacing: 6px;
    text-transform: uppercase;
    color: var(--on-red);
    line-height: 1;
  }
  .person-name {
    position: absolute;
    top: 235px;
    left: 0;
    right: 0;
    font-family: "Arvo", serif;
    font-weight: 400;
    font-size: 37px;
    line-height: 44px;
    color: var(--ink);
  }
  .person-title {
    position: absolute;
    top: 280px;
    left: 0;
    right: 0;
    font-family: "Arvo", serif;
    font-size: 24px;
    line-height: 28px;
    color: var(--muted);
  }
  .contact-list {
    position: absolute;
    top: 348px;
    left: 0;
    right: 0;
    list-style: none;
    font-family: "Arimo", sans-serif;
    font-size: 25px;
    line-height: 35px;
    color: var(--ink);
  }
  .contact-label {
    font-weight: 700;
    color: var(--brand-red);
    margin-right: 14px;
  }
</style>
</head>
<body>
  <main class="canvas">
    <section class="card card--front" aria-label="Card front">
      <div class="wordmark wordmark--front">Bright-loop designs</div>
      <h1 class="person-name">Corin Maltby</h1>
      <p class="person-title">Title</p>
      <ul class="contact-list">
        <li><span class="contact-label">m:</span>868 512-7361</li>
        <li><span class="contact-label">e:</span>bright_loopdesigns@mailbrook.net</li>
        <li><span class="contact-label">w:</span>www.brightloopdesigns.net</li>
      </ul>
    </section>
    <section class="card card--back" aria-label="Card back">
      <div class="wordmark wordmark--back">Bright-loop designs</div>
      <p class="tagline">embroidery &amp; artwork</p>
    </section>
  </main>
</body>
</html>
```